Builder Supply Needs Eye-catching Poster Design for Upcoming Workshop

We're doing a concrete carving workshop. It's a new concept in our area. We need a poster that will get people asking questions about it.

Needs to have:
- Our logo somewhere
- Picture(s) of concrete carving (attached)
- Should say, "We're hosting a vertical carving workshop. Details to be announced. Sign up for more information"

Target Market(s)

Contractors

Industry/Entity Type

Concrete

Font styles to use
Sans Serif

Requirements
Must have
• - Our logo somewhere
• - Picture(s) of concrete carving (attached)
• - Should say, "We're hosting a vertical carving workshop. Details to be announced. Sign up for more information"
• - Needs to be high enough resolution to be printed at 24 x 36 by Quillo Press
Nice to have
• Eye-catching design

```html
<!DOCTYPE html>
<html lang="en">
<head>
<meta charset="utf-8">
<title>Vertical Carving Workshop – Calder Concrete Supply</title>
<link rel="stylesheet" href="https://fonts.googleapis.com/css2?family=Montserrat:wght@500;600;700&family=Rubik+Dirt&display=swap">
<style>
  :root {
    --concrete-dark: #3f4042;
    --concrete-mid: #6c6d70;
    --concrete-light: #9a9b9e;
    --stripe: rgba(255, 255, 255, 0.13);
    --ink-white: #ffffff;
    --brand-blue: #1f73b7;
    --detail-blue: #8ec3ea;
    --outline: #2b2c2e;
  }
  * { margin: 0; padding: 0; box-sizing: border-box; }
  html, body { width: 800px; height: 1200px; overflow: hidden; background: #2a2a2a; }
  .poster {
    position: relative;
    width: 800px;
    height: 1200px;
    overflow: hidden;
    background:
      repeating-linear-gradient(-55deg, transparent 0 95px, var(--stripe) 95px 190px),
      radial-gradient(ellipse at 50% 40%, var(--concrete-light) 0%, var(--concrete-mid) 45%, var(--concrete-dark) 100%);
    font-family: "Montserrat", Arial, sans-serif;
    color: var(--ink-white);
  }
  .brand {
    position: absolute;
    top: 50px;
    left: 0;
    width: 100%;
    display: flex;
    justify-content: center;
    align-items: center;
    gap: 14px;
  }
  .brand-square {
    width: 34px;
    height: 34px;
    background: var(--brand-blue);
  }
  .brand-name {
    font-weight: 700;
    font-size: 32px;
    letter-spacing: 2px;
    text-transform: uppercase;
    color: var(--ink-white);
  }
  .intro {
    position: absolute;
    top: 270px;
    left: 48px;
    font-weight: 600;
    font-size: 32px;
    letter-spacing: 1px;
    text-transform: uppercase;
  }
  .headline {
    position: absolute;
    top: 318px;
    left: 30px;
    width: 740px;
    text-align: center;
    font-family: "Rubik Dirt", Impact, sans-serif;
    font-weight: 400;
    text-transform: uppercase;
    color: var(--ink-white);
    -webkit-text-stroke: 3px var(--outline);
    paint-order: stroke fill;
    line-height: 0.98;
    white-space: nowrap;
  }
  .headline span { display: block; }
  .headline .line-1 { font-size: 128px; }
  .headline .line-2 { font-size: 128px; }
  .headline .line-3 { font-size: 112px; margin-top: 4px; }
  .details {
    position: absolute;
    top: 712px;
    left: 0;
    width: 100%;
    text-align: center;
    font-weight: 500;
    font-size: 29px;
    line-height: 1.2;
    letter-spacing: 1px;
    text-transform: uppercase;
    color: var(--detail-blue);
  }
  .gallery {
    position: absolute;
    top: 852px;
    left: 0;
    width: 100%;
    height: 136px;
    display: flex;
    gap: 4px;
    padding: 0 2px;
  }
  .gallery-photo { flex: 1; height: 100%; }
  .photo-wall { background: linear-gradient(160deg, #a79a88, #6e6457); }
  .photo-arch { background: linear-gradient(180deg, #8fa7b4, #7a6a57 60%, #4e5b3d); }
  .photo-grotto { background: linear-gradient(170deg, #b9b3a7, #857a6c); }
  .photo-stone { background: linear-gradient(150deg, #cfcac0, #9b968c); }
  .photo-ledge { background: linear-gradient(165deg, #8b7a68, #5d4f42); }
  .web-band {
    position: absolute;
    top: 1110px;
    left: 0;
    width: 100%;
    height: 60px;
    background: var(--ink-white);
    display: flex;
    align-items: center;
    justify-content: center;
    font-weight: 700;
    font-size: 28px;
    letter-spacing: 4px;
    color: var(--brand-blue);
  }
</style>
</head>
<body>
  <main class="poster">
    <header class="brand">
      <div class="brand-square"></div>
      <div class="brand-name">Calder Concrete Supply</div>
    </header>

    <p class="intro">We're hosting a</p>

    <h1 class="headline">
      <span class="line-1">Vertical</span>
      <span class="line-2">Carving</span>
      <span class="line-3">Workshop</span>
    </h1>

    <p class="details">Details to be announced<br>Sign up for more information</p>

    <section class="gallery">
      <div class="gallery-photo photo-wall" role="img" aria-label="Photo of a carved concrete rock wall"></div>
      <div class="gallery-photo photo-arch" role="img" aria-label="Photo of a carved concrete stone archway in a garden"></div>
      <div class="gallery-photo photo-grotto" role="img" aria-label="Photo of a carved concrete rock feature"></div>
      <div class="gallery-photo photo-stone" role="img" aria-label="Photo of carved flagstone-pattern concrete wall"></div>
      <div class="gallery-photo photo-ledge" role="img" aria-label="Photo of carved ledgestone concrete wall"></div>
    </section>

    <footer class="web-band">WWW.CALDERCONCRETE.COM</footer>
  </main>
</body>
</html>
```